Banner required for our website Sale of Silent Domestic Rangehoods

These images around silence are very good however, even more important are the family conversations that happen within the kitchen area.
These conversations are often disrupted by the use of a noisy rangehood.
A Family photos in the kitchen with a tag line relating to regaining those precious moments would be a great concept.
Regards Neil
Just a few suggestions.
I would prefer no illistrations.
Most importantly I am still seeking a visual to highlite the silent benifit of our rangehoods.The best visual will most like win this contest. We currently use the lady with the finger held to her mouth. Any other suggestions would be greatly appreciated.
We need a banner ad for the sale of designer silent domestic rangehoods.
These rangehood are aimed at the middle to higher income buyers, they are Elegant, efficient and powerful.
We aim to offer a product that exceeds our customers expectations.
Visit our website and everything we do is self explainatory.
www.mirovale.com.au
Regards Neil
Updates
Mirovale Silent rangehoods enable the family to again enjoy conversations in the kitchen
You can have friends over, revel in each others company and enjoy a great lunch or dinner without the distraction of a rangehood that sounds like a jet engine.
They also simply work better
Our promo banners typically have 2 sizes: 500x500 pixels for our socials, and a 2570*730 pixels for our Promotions page
Target Market(s)
Renovators, second home buyers, ladies between 28 and 49 years of age
Requirements
Must have
- Appealing visuals, upmarket look and feel.
Nice to have
- Family picture with kids.
Should not have
- The words Cheap, Budget nor afforadable.

```html
<!DOCTYPE html>
<html lang="en">
<head>
<meta charset="utf-8">
<title>Mirovale Silent Rangehoods</title>
<link rel="stylesheet" href="https://fonts.googleapis.com/css2?family=Inter:wght@400;500;700;900&display=swap">
<style>
  :root {
    --brand-pink: #e2126f;
    --nav-bg: rgba(55, 55, 55, 0.95);
    --nav-text: #ffffff;
    --ink: #0a0a0a;
    --white: #ffffff;
  }
  * { margin: 0; padding: 0; box-sizing: border-box; }
  html, body { width: 1200px; height: 681px; overflow: hidden; }
  body { font-family: "Inter", sans-serif; color: var(--ink); position: relative; background: #f4f1ee; }

  .hero-photo {
    position: absolute; inset: 0;
    background:
      radial-gradient(ellipse 260px 340px at 800px 230px, rgba(214,128,70,0.85), rgba(214,128,70,0) 70%),
      radial-gradient(ellipse 230px 260px at 860px 560px, rgba(80,150,200,0.85), rgba(80,150,200,0) 72%),
      radial-gradient(ellipse 200px 220px at 1020px 430px, rgba(225,222,218,0.9), rgba(225,222,218,0) 75%),
      linear-gradient(90deg, #f7f5f3 0%, #f1ede9 35%, #ece5de 60%, #e7ddd3 100%);
  }

  .site-nav {
    position: absolute; top: 0; left: 0; width: 1200px; height: 38px;
    background: var(--nav-bg);
    display: flex; align-items: center;
  }
  .brand {
    position: absolute; left: 261px; top: 8px;
    display: flex; align-items: center; gap: 6px;
    color: var(--nav-text); font-weight: 700; font-size: 16px; letter-spacing: -0.2px;
  }
  .brand-square { width: 12px; height: 12px; background: var(--brand-pink); }
  .nav-menu { position: absolute; top: 0; left: 485px; height: 38px; display: flex; align-items: center; list-style: none; }
  .nav-menu li {
    color: var(--nav-text); font-size: 9.5px; font-weight: 500;
    display: flex; align-items: center; gap: 5px; margin-right: 13px;
  }
  .nav-menu svg { width: 7px; height: 5px; }
  .nav-search { position: absolute; left: 915px; top: 12px; width: 13px; height: 13px; }

  .hero-copy { position: absolute; left: 260px; top: 151px; }
  .headline { font-weight: 900; font-size: 55px; line-height: 54px; letter-spacing: -0.5px; }
  .intro { margin-top: 3px; width: 300px; font-size: 11px; line-height: 13px; }
  .offer { margin-top: 20px; font-size: 27px; font-weight: 400; letter-spacing: -0.2px; line-height: 30px; }
  .offer strong { color: var(--brand-pink); font-weight: 700; }
  .actions { margin-top: 21px; display: flex; gap: 23px; }
  .btn {
    width: 142px; height: 33px; background: var(--brand-pink); color: var(--white);
    display: flex; align-items: center; padding-left: 16px; gap: 14px;
    font-size: 10px; font-weight: 500; text-decoration: none;
  }
  .btn svg { width: 15px; height: 12px; }
</style>
</head>
<body>
  <div class="hero-photo" role="img" aria-label="Smiling mother holding a baby in a blue sling, drinking from a white mug and looking at her phone in a bright kitchen"></div>

  <header class="site-nav">
    <div class="brand"><span class="brand-square"></span>mirovale</div>
    <ul class="nav-menu">
      <li>Products <svg viewBox="0 0 8 5"><path d="M1 1l3 3 3-3" stroke="#fff" stroke-width="1.5" fill="none"/></svg></li>
      <li>Promotions</li>
      <li>Get Inspired <svg viewBox="0 0 8 5"><path d="M1 1l3 3 3-3" stroke="#fff" stroke-width="1.5" fill="none"/></svg></li>
      <li>Media <svg viewBox="0 0 8 5"><path d="M1 1l3 3 3-3" stroke="#fff" stroke-width="1.5" fill="none"/></svg></li>
      <li>About <svg viewBox="0 0 8 5"><path d="M1 1l3 3 3-3" stroke="#fff" stroke-width="1.5" fill="none"/></svg></li>
      <li>Support <svg viewBox="0 0 8 5"><path d="M1 1l3 3 3-3" stroke="#fff" stroke-width="1.5" fill="none"/></svg></li>
      <li>Contact <svg viewBox="0 0 8 5"><path d="M1 1l3 3 3-3" stroke="#fff" stroke-width="1.5" fill="none"/></svg></li>
    </ul>
    <svg class="nav-search" viewBox="0 0 14 14"><circle cx="5.5" cy="5.5" r="4.2" stroke="#fff" stroke-width="2" fill="none"/><path d="M8.8 8.8L13 13" stroke="#fff" stroke-width="2.2" stroke-linecap="round"/></svg>
  </header>

  <main class="hero-copy">
    <h1 class="headline">Elegant.<br>Efficient.<br>Sssssilent...</h1>
    <p class="intro">Our silent rangehoods harness the power and efficiency of the German-engineered Quietcore® motor mounted outside your home, so you enjoy blissful silence where you cook.</p>
    <p class="offer">NOW ON <strong>SPECIAL PRICE</strong></p>
    <div class="actions">
      <a class="btn" href="#">Discover Silence <svg viewBox="0 0 16 12"><path d="M1 6h13M9 1l5 5-5 5" stroke="#fff" stroke-width="1.6" fill="none"/></svg></a>
      <a class="btn" href="#">Check Our Offer <svg viewBox="0 0 16 12"><path d="M1 6h13M9 1l5 5-5 5" stroke="#fff" stroke-width="1.6" fill="none"/></svg></a>
    </div>
  </main>
</body>
</html>
```